Need App for Impact Related Events

My app is to help with internal events. When you enter the prompted event code the next screen shows you everyone currently at the event. It will give you the ability to Start a conversation with someone you met at that event, or signal it is your turn to send a message. The next screen is a message thread with that person. I am looking for a design that incorporates the colors and ‘feel good’ emotion of our logo. I have pieced together a pretty good interpretation of what I’m looking for in the attached mockup by slicing and dicing designs. I also attached our logo mascot.Screens (see attached mockups)

Note 1: I do not like the picture on the screen used in screen one because it makes it seem like a dating app. I attached an alternative photo that can be used or present different ideas.

Note 2: On the login/signup screen (screen 2) I need an additional first and last name for login, you can try to fit this on one login screen or present a two step signup screen where that is presented in the second screen.

READ MOCKUP GUIDELINES UNDER Must Haves

Target Market(s)

People attending internal social impact events

Industry/Entity Type

Charity

Font styles to use
Sans Serif

Colors
86cfc6

Requirements
Must have
• Follow the screen mockups attached to project
• PLEASE READ
• I have provided a relatively close design of what I’m looking for in the mockups. Some screens need to be followed more closely to my design mockup than other. I have listed a guide below how how closely you should follow my mockup design exactly. Overall I would like to see some ideas of incorporating a few accent colors so it doesn’t appear SO Blue. I also attached some app inspiration designs I found from around the web
• Screen Mockup Guideline Follow %
• Screen 1: 65% - mostly on target, would like to see ways to make it not SO Blue and possibly creative places to add some explainer text describing the app
• Screen 2: 50% - general design idea is here, but more open
• Screen 3: 35% - a lot more room for design influence
• Screen 4: 70% - mostly on target, a little room for design influence/color scheme ideas
• Screen 5-6: 25% - a lot of room for design change/ideas/influence
• Screen 7-8: 80% - already very close to what I need, maybe open to slight sizing and color scheme ideas
• Screen 9: 15% - the most open for influence, only the general functionality of the screen is communicated here
Nice to have
• Please Read Mockup Guideline above. In large part I am looking for something to use some nice accent colors so it is not overwhelmingly blue and bring the whole design into a seamless style.
Should not have

```html
<!DOCTYPE html>
<html lang="en">
<head>
<meta charset="utf-8">
<title>Hive Hello – App Screens</title>
<link href="https://fonts.googleapis.com/css2?family=Lato:wght@400;700&display=swap" rel="stylesheet">
<style>
:root{
  --page:#ffffff;
  --screen:#68a69a;
  --screen-dark:#5e998d;
  --ink:#ffffff;
  --ink-soft:#d3ebe5;
  --ink-muted:#a9d3c9;
  --mark:#a8e9e0;
  --mascot-a:#2ec9cf;
  --mascot-b:#2d3b2c;
  --btn-light:#ffffff;
  --btn-dark-text:#2f3a38;
  --accent-a:#6fae8c;
  --accent-b:#98d89c;
  --social:#3a6f86;
  --chat-top:#d9ebe4;
  --chat-bottom:#f1f8ec;
  --bubble:#c6dfd5;
  --bubble-text:#4f6a62;
  --photo-a:#8c9a8e;
  --photo-b:#6f8f86;
  --avatar-a:#8e8f7f;
  --avatar-b:#5f7470;
}
*{box-sizing:border-box;margin:0;padding:0}
html,body{width:1200px;height:1200px;overflow:hidden;background:var(--page)}
body{font-family:'Lato',sans-serif;color:var(--ink);position:relative}
.screen{position:absolute;width:226px;height:488px;border-radius:24px;background:var(--screen);overflow:hidden}
.screen > *{position:absolute}
.s1{left:62px;top:50px}.s2{left:346px;top:50px}.s3{left:630px;top:50px}.s4{left:914px;top:50px}
.s5{left:62px;top:640px}.s6{left:346px;top:640px}.s7{left:630px;top:640px}.s8{left:914px;top:640px}

.hero-photo{left:0;top:0;width:226px;height:220px;background:linear-gradient(180deg,var(--photo-a) 0%,var(--photo-b) 55%,var(--screen) 100%)}
.mascot{left:65px;top:38px;width:96px;height:84px;border-radius:42px;background:radial-gradient(circle at 60% 45%,var(--mascot-a) 0%,var(--mascot-a) 45%,var(--mascot-b) 70%,transparent 72%)}
.s1 .mascot{top:146px}
.wordmark{left:0;width:226px;top:140px;text-align:center;font-size:21px;font-weight:400;color:var(--mark);letter-spacing:.5px}
.s1 .wordmark{top:244px}
.blurb{left:20px;width:186px;top:274px;text-align:center;font-size:6.5px;line-height:9.5px;color:var(--ink-muted)}
.title{left:0;width:226px;top:192px;text-align:center;font-size:14px;color:var(--ink)}

.btn{width:105px;height:22px;display:flex;align-items:center;justify-content:center;font-size:9px}
.btn-light{background:var(--btn-light);color:var(--btn-dark-text);font-weight:700;box-shadow:0 2px 4px rgba(0,0,0,.12)}
.btn-accent{background:linear-gradient(90deg,var(--accent-a),var(--accent-b));color:var(--ink);box-shadow:0 3px 6px rgba(0,0,0,.12)}
.at-login{left:22px;top:352px}
.at-create{left:22px;top:404px}
.at-center-low{left:61px;top:404px}

.field-label{left:30px;font-size:7px;color:var(--ink-muted)}
.field-line{left:30px;width:176px;height:1px;background:rgba(255,255,255,.3)}
.small{font-size:6.5px;color:var(--ink)}
.social-btn{left:23px;top:404px;width:105px;height:22px;background:var(--social);display:flex;align-items:center;gap:5px;padding-left:5px;font-size:8px;color:var(--ink)}
.social-btn i{display:block;width:11px;height:11px;background:var(--ink);border-radius:2px}
.legal{left:20px;width:186px;top:454px;text-align:center;font-size:6.5px;line-height:9.5px;color:var(--ink-muted)}
.legal b{color:var(--ink);font-weight:400}

.avatar-slot{left:59px;top:250px;width:107px;height:107px;background:rgba(150,210,170,.35);display:flex;align-items:center;justify-content:center}
.add-badge{left:152px;top:342px}
.skip{left:0;width:226px;top:462px;text-align:center;font-size:6.5px;color:var(--btn-dark-text)}
.input-box{left:30px;top:238px;width:166px;height:30px;border:1px solid rgba(255,255,255,.45);border-radius:2px}
.kind-code{left:0;width:226px;top:252px;text-align:center;font-size:13px;letter-spacing:.3px}
.code-note{left:20px;width:186px;top:286px;text-align:center;font-size:8.5px;line-height:14.5px;color:var(--ink-muted)}

.nav-icon{top:39px}
.nav-back{left:13px}.nav-settings{left:198px}
.list-title{left:0;width:226px;top:64px;text-align:center;font-size:14px}
.person{left:14px;width:198px;height:44px;display:flex;align-items:center}
.face{width:44px;height:44px;border-radius:50%;background:linear-gradient(135deg,var(--avatar-a),var(--avatar-b));flex:none}
.person-name{margin-left:20px;font-size:8.5px;flex:1}
.person-note{font-size:6.5px;color:var(--mark)}
.show-more{left:61px;top:450px}

.chat-band{left:0;top:111px;width:226px;height:377px;background:linear-gradient(180deg,var(--chat-top),var(--chat-bottom))}
.chat-head{left:13px;top:85px;width:50px;height:50px;border-radius:50%;background:linear-gradient(135deg,var(--avatar-a),var(--avatar-b));border:2px solid var(--chat-top)}
.chat-name{left:70px;top:93px;font-size:11.5px;font-weight:700}
.bubble{width:137px;height:38px;background:var(--bubble);color:var(--bubble-text);font-size:6.5px;line-height:12px;padding:6px 12px}
.bubble.in{left:28px}.bubble.out{left:60px}
.mini-face{width:34px;height:34px;border-radius:50%;background:linear-gradient(135deg,var(--avatar-a),var(--avatar-b))}
.typing{left:20px;top:439px;font-size:4.5px;color:var(--bubble-text)}
.chat-input{left:16px;top:450px;width:194px;height:22px;border:1px solid rgba(104,166,154,.3);background:rgba(255,255,255,.4);font-size:6.5px;color:var(--bubble-text);padding:6px 10px}
.send-hint{left:152px;top:475px;font-size:6.5px;color:var(--btn-dark-text);display:flex;align-items:center;gap:6px}
</style>
</head>
<body>

<!-- Welcome -->
<section class="screen s1">
  <div class="hero-photo" role="img" aria-label="Group of friends chatting at a lively event"></div>
  <div class="mascot" role="img" aria-label="Smiling bee mascot illustration"></div>
  <div class="wordmark">Hive Hello</div>
  <p class="blurb">Lorem ipsum dolor sit amet, consectetur adipisicing elit, sed do eiusmod tempor incididunt ut labore et</p>
  <div class="btn btn-light at-login">Login</div>
  <div class="btn btn-accent at-create">Create new user</div>
</section>

<!-- Login -->
<section class="screen s2">
  <div class="mascot" role="img" aria-label="Smiling bee mascot illustration"></div>
  <div class="wordmark">Hive Hello</div>
  <span class="field-label" style="top:224px">Email or Username</span>
  <span class="field-line" style="top:240px"></span>
  <span class="field-label" style="top:269px">Password (6 + Characters)</span>
  <span class="field-line" style="top:285px"></span>
  <div class="btn btn-light" style="left:23px;top:301px">Login</div>
  <span class="small" style="left:23px;top:339px">Forgot passsword?</span>
  <span class="small" style="left:23px;top:390px">Or, Sign up with</span>
  <div class="social-btn"><i></i>Continue with Socialnet</div>
  <p class="legal">By signing up, you agree to our <b>Terms of Use</b><br>and <b>Privacy Policy.</b></p>
</section>

<!-- Profile picture -->
<section class="screen s3">
  <div class="mascot" role="img" aria-label="Smiling bee mascot illustration"></div>
  <div class="wordmark">Hive Hello</div>
  <div class="title">Add Profile Picture</div>
  <div class="avatar-slot">
    <svg width="42" height="56" viewBox="0 0 42 56"><circle cx="21" cy="16" r="12" fill="#4f7f72"/><path d="M2 56 Q2 32 21 32 Q40 32 40 56 Z" fill="#4f7f72"/></svg>
  </div>
  <svg class="add-badge" width="22" height="22" viewBox="0 0 22 22"><circle cx="11" cy="11" r="10" fill="#7fc49a" stroke="#a9dcb6" stroke-width="1.5"/><path d="M11 5v12M5 11h12" stroke="#e7f6ec" stroke-width="2.4"/></svg>
  <div class="skip">Skip for now</div>
</section>

<!-- Location name -->
<section class="screen s4">
  <div class="mascot" role="img" aria-label="Smiling bee mascot illustration"></div>
  <div class="wordmark">Hive Hello</div>
  <div class="title">Give Your Location a Name</div>
  <div class="input-box"></div>
  <div class="btn btn-accent at-center-low">Get Your Code</div>
</section>

<!-- Enter code -->
<section class="screen s5">
  <div class="mascot" role="img" aria-label="Smiling bee mascot illustration"></div>
  <div class="wordmark">Hive Hello</div>
  <div class="title">Enter Location Kind Code</div>
  <div class="input-box"></div>
  <div class="btn btn-light" style="left:61px;top:290px">Submit</div>
  <div class="btn btn-accent at-center-low">Create a Kind Code</div>
</section>

<!-- Your code -->
<section class="screen s6">
  <div class="mascot" role="img" aria-label="Smiling bee mascot illustration"></div>
  <div class="wordmark">Hive Hello</div>
  <div class="title">Your Kind Code</div>
  <div class="kind-code">AA434564CN3423</div>
  <p class="code-note">Give this code tothe people at your location or vent to allow them to connect to ech other - kind of like a wifi password.</p>
  <div class="btn btn-accent at-center-low">Manage Settings</div>
</section>

<!-- People met -->
<section class="screen s7">
  <svg class="nav-icon nav-back" width="15" height="15" viewBox="0 0 15 15"><circle cx="7.5" cy="7.5" r="6.5" fill="none" stroke="#fff" stroke-width="1"/><path d="M8.8 4.5 5.8 7.5l3 3" fill="none" stroke="#fff" stroke-width="1"/></svg>
  <svg class="nav-icon nav-settings" width="15" height="15" viewBox="0 0 15 15"><circle cx="7.5" cy="7.5" r="6.5" fill="none" stroke="#fff" stroke-width="1"/><circle cx="7.5" cy="7.5" r="2.6" fill="none" stroke="#fff" stroke-width="1.6" stroke-dasharray="1.4 1"/></svg>
  <div class="list-title">Who you’ve met so far</div>

  <div class="person" style="top:110px"><span class="face" role="img" aria-label="Portrait photo of Owen"></span><span class="person-name">Owen</span>
    <svg width="16" height="16" viewBox="0 0 16 16"><circle cx="8" cy="8" r="7" fill="none" stroke="#fff"/><path d="M6.5 5v6l4.5-3z" fill="#fff"/></svg></div>
  <div class="person" style="top:164px"><span class="face" role="img" aria-label="Portrait photo of Lena"></span><span class="person-name">Lena</span>
    <svg width="16" height="16" viewBox="0 0 16 16"><circle cx="8" cy="8" r="7" fill="none" stroke="#8fd39c"/><path d="M5 8h6M8.5 5.5 11 8l-2.5 2.5" fill="none" stroke="#8fd39c"/></svg></div>
  <div class="person" style="top:219px"><span class="face" role="img" aria-label="Portrait photo of Theo"></span><span class="person-name">Theo</span>
    <svg width="16" height="16" viewBox="0 0 16 16"><circle cx="8" cy="8" r="7" fill="none" stroke="#fff"/><path d="M6.5 5v6l4.5-3z" fill="#fff"/></svg></div>
  <div class="person" style="top:273px"><span class="face" role="img" aria-label="Portrait photo of Rafe"></span><span class="person-name">Rafe</span><span class="person-note">Great Idea...</span></div>
  <div class="person" style="top:328px"><span class="face" role="img" aria-label="Portrait photo of Jonah"></span><span class="person-name">Jonah</span><span class="person-note">Cool meeting...</span></div>
  <div class="person" style="top:382px"><span class="face" role="img" aria-label="Portrait photo of Priya"></span><span class="person-name">Priya</span><span class="person-note">Good speech...</span></div>

  <div class="btn btn-accent show-more">Show more</div>
</section>

<!-- Chat thread -->
<section class="screen s8">
  <svg class="nav-icon nav-back" width="15" height="15" viewBox="0 0 15 15"><circle cx="7.5" cy="7.5" r="6.5" fill="none" stroke="#fff" stroke-width="1"/><path d="M8.8 4.5 5.8 7.5l3 3" fill="none" stroke="#fff" stroke-width="1"/></svg>
  <svg class="nav-icon nav-settings" width="15" height="15" viewBox="0 0 15 15"><circle cx="7.5" cy="7.5" r="6.5" fill="none" stroke="#fff" stroke-width="1"/><circle cx="7.5" cy="7.5" r="2.6" fill="none" stroke="#fff" stroke-width="1.6" stroke-dasharray="1.4 1"/></svg>
  <div class="chat-band"></div>
  <div class="chat-head" role="img" aria-label="Portrait photo of Maren Holt"></div>
  <div class="chat-name">Maren Holt</div>

  <p class="bubble in" style="top:148px">Hey have you seen the stuff I have been  working on lately?</p>
  <span class="mini-face" style="left:176px;top:148px" role="img" aria-label="Portrait photo of Lena"></span>
  <span class="mini-face" style="left:15px;top:218px" role="img" aria-label="Portrait photo of Maren Holt"></span>
  <p class="bubble out" style="top:216px">Wow! I saw those ideas.  I will add more to that one.</p>

  <p class="bubble in" style="top:284px">Hey have you seen the stuff I have been  working on lately?</p>
  <span class="mini-face" style="left:176px;top:284px" role="img" aria-label="Portrait photo of Lena"></span>
  <span class="mini-face" style="left:15px;top:354px" role="img" aria-label="Portrait photo of Maren Holt"></span>
  <p class="bubble out" style="top:352px">Wow! I saw those ideas.  I will add more to that one.</p>

  <span class="typing">Lena typing...</span>
  <div class="chat-input">I was thinking |</div>
  <div class="send-hint"><svg width="8" height="8" viewBox="0 0 8 8"><circle cx="4" cy="4" r="3.4" fill="none" stroke="#2f3a38" stroke-width=".8"/><circle cx="4" cy="4" r="1.2" fill="#2f3a38"/></svg>Enter to send</div>
</section>

</body>
</html>
```